New Property development signage

large poster for a new development.
3 metres x 2 metres. To include the following.

Varnock Meadows
TO LET
LUXURY FULLY FURNISHED LARGE
2 AND 3 BED APARTMENTS
Tilwick Estates
362 4159
www.tilwickestates-example.com

Need this to be large simple writing with Tilwick estates logo on the bottom

Target Market(s)

High end rental property market

Industry/Entity Type

Real Estate Development

Colors
000000
cbcbcb
0555a3

Requirements
Must have
• Name of the development must be in a different font, classic style
Nice to have
• Light Grey background, blues for colours
Should not have
• anymore than 3 /4 colours

```html
<!DOCTYPE html>
<html lang="en">
<head>
<meta charset="utf-8">
<title>Varnock Meadows – To Let</title>
<link rel="stylesheet" href="https://fonts.googleapis.com/css2?family=Anton&family=Lobster&family=Arimo:wght@700&family=Roboto+Condensed:wght@700&family=Libre+Baskerville:wght@400&display=swap">
<style>
  :root {
    --brand-blue: #03508c;
    --sign-red: #e2000f;
    --paper: #ffffff;
    --ink: #1a1a1a;
    --logo-blue: #2b3990;
  }
  * { margin: 0; padding: 0; box-sizing: border-box; }
  html, body { width: 1200px; height: 800px; overflow: hidden; background: var(--paper); }
  .sign { position: relative; width: 1200px; height: 800px; background: var(--paper); overflow: hidden; }

  .development-band {
    position: absolute; left: 0; top: 0; width: 1200px; height: 200px;
    background: var(--brand-blue);
    display: flex; align-items: center; justify-content: center;
  }
  .development-name {
    font-family: "Anton", "Impact", sans-serif;
    font-size: 148px; line-height: 1; letter-spacing: 2px;
    color: var(--paper); text-transform: uppercase; white-space: nowrap;
    padding-top: 6px;
  }

  .offer-band {
    position: absolute; left: 0; top: 200px; width: 1200px; height: 325px;
    background: var(--sign-red); color: var(--paper); text-align: center;
  }
  .offer-headline {
    font-family: "Anton", "Impact", sans-serif;
    font-size: 120px; line-height: 1; margin-top: 6px;
    letter-spacing: 2px; text-transform: uppercase;
  }
  .offer-details {
    font-family: "Lobster", cursive;
    font-size: 72px; line-height: 86px; margin-top: 14px; white-space: nowrap;
  }

  .contact-phone {
    position: absolute; left: 38px; top: 540px;
    font-family: "Arimo", "Arial", sans-serif; font-weight: 700;
    font-size: 190px; line-height: 1; color: var(--ink); white-space: nowrap;
    transform: scaleX(0.86); transform-origin: left top;
  }
  .contact-web {
    position: absolute; left: 40px; top: 703px;
    font-family: "Roboto Condensed", "Arial Narrow", sans-serif; font-weight: 700;
    font-size: 48px; line-height: 1; color: var(--ink); white-space: nowrap;
  }

  .agency {
    position: absolute; left: 752px; top: 557px; width: 408px; height: 191px;
    display: flex; flex-direction: column; align-items: center; justify-content: center; gap: 22px;
  }
  .agency-name-row { display: flex; align-items: center; gap: 14px; white-space: nowrap; }
  .agency-mark { flex: none; width: 26px; height: 26px; background: var(--sign-red); }
  .agency-name {
    font-family: "Libre Baskerville", "Georgia", serif; font-weight: 400;
    font-size: 40px; line-height: 1; color: var(--logo-blue);
  }
  .agency-services {
    font-family: "Libre Baskerville", "Georgia", serif;
    font-size: 15px; color: var(--ink); letter-spacing: 0.3px; white-space: nowrap;
  }
</style>
</head>
<body>
  <main class="sign">
    <header class="development-band">
      <h1 class="development-name">Varnock Meadows</h1>
    </header>

    <section class="offer-band">
      <p class="offer-headline">To Let</p>
      <p class="offer-details">Luxury Fully Furnished Large<br>2 and 3 Bed Apartments</p>
    </section>

    <p class="contact-phone">362 4159</p>
    <p class="contact-web">www.tilwickestates-example.com</p>

    <aside class="agency">
      <div class="agency-name-row">
        <span class="agency-mark"></span>
        <span class="agency-name">Tilwick Estates</span>
      </div>
      <p class="agency-services">Sales • Lettings • Management • B.E.R. Certs</p>
    </aside>
  </main>
</body>
</html>
```